Business Card Design Project

We need a Business Card for an Mechanical Engineering firm in Singapore. The design should be Modern & Technical looking, yet eye catching.

Our company deals in Cutting Tools & Machine Accessories for the Manufacturing Industries such as Oil & Gas, Aero Space, etc... For more information on our Company, you can either email me or view our website www.valtrion.com.sg.

We are trying to revamp our image to give our consumers a fresh new perspective to our company, so we welcome all ideas.

Industry/Entity Type

Business

Requirements
Must have
• Must incorporate New Company Logo into the card as shown in Uploaded file.

```html
<!DOCTYPE html>
<html lang="en">
<head>
<meta charset="utf-8">
<title>Valtrion Tools – Business Card</title>
<link rel="stylesheet" href="https://fonts.googleapis.com/css2?family=Arimo:wght@400;700&family=Open+Sans:wght@700&family=Oswald:wght@400&display=swap">
<style>
  :root {
    --page-bg: #f2f2f2;
    --card-bg: #ffffff;
    --brand-crimson: #9b0032;
    --brand-crimson-light: #a80a3c;
    --brand-crimson-dark: #8a002c;
    --ink-maroon: #3a0b1c;
    --text-light: #ffffff;
  }

  * { margin: 0; padding: 0; box-sizing: border-box; }

  html, body {
    width: 750px;
    height: 1200px;
    overflow: hidden;
    background: var(--page-bg);
  }

  .business-card {
    position: absolute;
    left: 75px;
    top: 75px;
    width: 600px;
    height: 1050px;
    background: var(--card-bg);
  }

  .contact-panel {
    position: absolute;
    left: 22px;
    top: 22px;
    width: 558px;
    height: 536px;
    overflow: hidden;
  }

  .gear-texture {
    position: absolute;
    inset: 0;
    background:
      radial-gradient(circle at 84% 22%, var(--brand-crimson-light) 0%, var(--brand-crimson) 38%, transparent 39%),
      radial-gradient(circle at 17% 58%, var(--brand-crimson-light) 0%, var(--brand-crimson) 42%, transparent 43%),
      linear-gradient(160deg, var(--brand-crimson) 0%, var(--brand-crimson-dark) 100%);
  }

  .contact-details {
    position: absolute;
    left: 21px;
    top: 38px;
    color: var(--text-light);
    font-family: "Arimo", Arial, sans-serif;
  }

  .contact-name {
    font-size: 50px;
    font-weight: 400;
    font-variant: small-caps;
    letter-spacing: 1.5px;
    line-height: 1;
  }

  .job-title {
    font-size: 28px;
    font-variant: small-caps;
    letter-spacing: 1px;
    line-height: 1;
    margin-top: 4px;
  }

  .contact-lines {
    list-style: none;
    margin-top: 24px;
    font-size: 22px;
    letter-spacing: 0.5px;
  }

  .contact-lines li { line-height: 38px; }

  .brand-lockup {
    position: absolute;
    left: 0;
    top: 880px;
    width: 600px;
    display: flex;
    align-items: center;
    justify-content: center;
    gap: 16px;
  }

  .brand-mark {
    width: 52px;
    height: 52px;
    border-radius: 50%;
    background: var(--brand-crimson);
  }

  .brand-name {
    font-family: "Oswald", "Arial Narrow", sans-serif;
    font-weight: 400;
    font-size: 66px;
    line-height: 1;
    color: var(--brand-crimson);
    letter-spacing: 1px;
  }

  .website {
    position: absolute;
    left: 0;
    top: 993px;
    width: 600px;
    text-align: center;
    font-family: "Open Sans", Arial, sans-serif;
    font-weight: 700;
    font-size: 26px;
    color: var(--ink-maroon);
  }
</style>
</head>
<body>
  <main class="business-card">
    <section class="contact-panel">
      <div class="gear-texture" role="img" aria-label="Embossed interlocking gear pattern in crimson"></div>
      <div class="contact-details">
        <h1 class="contact-name">Contact Name</h1>
        <p class="job-title">Job Title</p>
        <ul class="contact-lines">
          <li>123.456.7890</li>
          <li>098.765.4321</li>
          <li>contact@valtriontools.com</li>
        </ul>
      </div>
    </section>

    <div class="brand-lockup">
      <span class="brand-mark"></span>
      <span class="brand-name">VALTRION TOOLS</span>
    </div>

    <p class="website">www.valtriontools.com</p>
  </main>
</body>
</html>
```